Newspaper AD in the Restaurant Section HOMECARE/Senior Living

Looking for an ad that is 6.425 inches wide and 5 inches tall to go into the newspaper weekly it will be in the restaurant section. We are a senior homecare company and we are looking to show clients that caregivers are able to assist them not only in personal care needs but also meal prep. We would like the design to have the feel of our existing ad or our newly launched website. It will be in the Savor section of the Kailani Courier which is not where we normally would advertise as a homecare agency so ad has to have some kind of feel for that section.
It should say somewhere maybe by contact info Call today for FREE Consultation.

Target Market(s)

Target market is Men/Women ages 35-105

Industry/Entity Type

Homecare and Senior Living

Font styles to use
Sans Serif

Colors
0054AA
0677BA
7BADD7
CADEEF
E8F1F8
FFF300
FFF600
FEFA6F
FFFEC7
FFFEE8
EB3D1F
EC4F4E
F09395
F8D3D4
FCEDEE

Requirements
Must have
• Logo, Contact info: Phone number (808) 555-0173, email address Info@brightmorehome.com and website www.Brightmorehome.com.
Nice to have
• Something that will be eye catching and to the point. Maybe a picture of a caregiver preparing a meal with an elderly person

```html
<!DOCTYPE html>
<html lang="en">
<head>
<meta charset="utf-8">
<title>Brightmore Homecare – Savor Section Ad</title>
<link href="https://fonts.googleapis.com/css2?family=Montserrat:wght@500;600;700&display=swap" rel="stylesheet">
<style>
  :root {
    --teal: #136e63;
    --salmon: #f49c84;
    --white: #ffffff;
    --ink: #1c1c1c;
    --page: #e9eaec;
    --fade: #ececec;
  }
  * { box-sizing: border-box; margin: 0; padding: 0; }
  html, body { width: 900px; height: 1200px; overflow: hidden; }
  body {
    background: var(--page);
    font-family: "Montserrat", Arial, sans-serif;
    position: relative;
  }
  .ad {
    position: absolute;
    left: 20px; top: 265px;
    width: 860px; height: 670px;
    background: linear-gradient(to bottom, var(--white) 80%, var(--fade) 88%, var(--white) 96%);
    overflow: hidden;
    box-shadow: 0 2px 6px rgba(0,0,0,0.25);
  }
  .ad__shapes { position: absolute; inset: 0; }
  .brand {
    position: absolute;
    left: 0; top: 40px; width: 330px;
    display: flex; flex-direction: column; align-items: center; gap: 14px;
  }
  .brand__mark {
    width: 50px; height: 50px;
    background: var(--salmon);
    border-radius: 8px;
  }
  .brand__name {
    font-weight: 700; font-size: 27px;
    color: var(--teal);
    letter-spacing: 0.5px;
  }
  .intro {
    position: absolute;
    left: 24px; top: 208px; width: 360px;
    color: var(--white);
    font-weight: 500; font-size: 17.5px; line-height: 22px;
  }
  .services {
    position: absolute;
    left: 37px; top: 286px;
    list-style: none;
    color: var(--white);
    font-weight: 700; font-size: 21px;
  }
  .services li { height: 45px; }
  .services li::before { content: "• "; }
  .cta {
    position: absolute;
    left: 206px; top: 504px; width: 448px; height: 86px;
    background: var(--salmon);
    border: 6px solid var(--white);
    text-align: center;
  }
  .cta__lead {
    display: block;
    color: var(--white);
    font-weight: 600; font-size: 20px;
    margin-top: 3px;
  }
  .cta__offer {
    display: block;
    color: var(--teal);
    font-weight: 700; font-size: 33px;
    line-height: 36px;
  }
  .contact {
    position: absolute;
    left: 0; width: 100%;
    text-align: center;
    color: var(--ink);
    font-weight: 500;
  }
  .contact--phone { top: 595px; font-size: 17px; }
  .contact--phone strong { color: var(--teal); font-weight: 700; font-size: 24px; }
  .contact--web { top: 630px; font-size: 16.5px; }
  .contact--web strong { font-weight: 700; }
</style>
</head>
<body>
  <section class="ad">
    <svg class="ad__shapes" width="860" height="670" viewBox="0 0 860 670">
      <defs>
        <linearGradient id="mealScene" x1="0" y1="0" x2="1" y2="1">
          <stop offset="0" stop-color="#7a3a24"/>
          <stop offset="0.45" stop-color="#c9c7a4"/>
          <stop offset="0.75" stop-color="#9b3346"/>
          <stop offset="1" stop-color="#6b3a22"/>
        </linearGradient>
      </defs>
      <polygon class="teal-band" points="0,177 373,177 545,548 0,548" fill="var(--teal)"/>
      <polygon class="meal-photo" role="img" aria-label="Photo: caregiver in scrubs serving a fresh fruit breakfast to an older couple at their dining table" points="291,0 860,0 860,548 545,548" fill="url(#mealScene)"/>
      <polygon class="accent-stripe" points="280,0 293,0 547,548 534,548" fill="var(--salmon)"/>
      <rect class="rule rule--salmon" x="0" y="655" width="860" height="3" fill="var(--salmon)"/>
      <rect class="rule rule--teal" x="0" y="662" width="860" height="8" fill="var(--teal)"/>
    </svg>

    <div class="brand">
      <span class="brand__mark"></span>
      <span class="brand__name">Brightmore Homecare</span>
    </div>

    <p class="intro">Personal care services to meet your loved ones needs in the comfort and safety of their own home.</p>

    <ul class="services">
      <li>Home Health Aides</li>
      <li>Skilled Nursing (RN/LPN)</li>
      <li>Bathing &amp; Meal Service</li>
      <li>Medication Management</li>
      <li>Services Available 24/7</li>
    </ul>

    <div class="cta">
      <span class="cta__lead">CALL TODAY FOR</span>
      <span class="cta__offer">FREE CONSULTATION</span>
    </div>

    <p class="contact contact--phone">Contact info: Phone number <strong>(808) 555-0173</strong></p>
    <p class="contact contact--web">Email: <strong>Info@brightmorehome.com</strong>&nbsp; website <strong>www.Brightmorehome.com</strong></p>
  </section>
</body>
</html>
```